Business Card Design for a Software Startup

We'd like to have a business card design. We already have a logo. Basically what we need is a clean design with name, address, cellphone and phone numbers, e-mail and web site address (front) and a space on the back with our logo with the company name on the right side and some texts on the bottom.
We are a development and consulting company in Brazil with highly qualified team of professionals in Java, iOS and Android development and consulting.

Target Market(s)

CIO, IT managers of mid to big size companies

Industry/Entity Type

Business

```html
<!DOCTYPE html>
<html lang="en">
<head>
<meta charset="utf-8">
<title>NOVKA Business Card</title>
<link rel="stylesheet" href="https://fonts.googleapis.com/css2?family=Open+Sans:wght@400;600;700&display=swap">
<style>
  :root {
    --backdrop: #3b3b3b;
    --card: #ffffff;
    --brand: #1f5a9a;
    --brand-light: #1aa0db;
    --navy: #2b4f86;
    --ink: #5a5a5a;
    --rule: #c9c9c9;
    --haze: #dceaf3;
  }
  * { margin: 0; padding: 0; box-sizing: border-box; }
  html, body {
    width: 978px; height: 1200px; overflow: hidden;
    background: var(--backdrop);
    font-family: "Open Sans", Arial, sans-serif;
  }
  .card {
    position: absolute; left: 78px; width: 831px; height: 489px;
    background: var(--card); overflow: hidden;
  }
  .card--front { top: 74px; }
  .card--back { top: 637px; }
  .card__decor { position: absolute; inset: 0; width: 100%; height: 100%; }

  .brand-block { position: absolute; left: 104px; top: 111px; width: 224px; text-align: center; }
  .brand-mark {
    width: 218px; height: 214px; margin: 0 auto;
    background: linear-gradient(135deg, var(--brand-light), var(--brand));
    border-radius: 26px;
  }
  .brand-name {
    font-weight: 700; color: var(--brand);
    font-size: 60px; line-height: 1; margin-top: 6px; letter-spacing: 0;
  }
  .divider {
    position: absolute; left: 393px; top: 107px; width: 2px; height: 280px;
    background: var(--rule);
  }
  .contact { position: absolute; left: 461px; top: 104px; color: var(--ink); }
  .contact__name { font-weight: 700; color: var(--navy); font-size: 25px; line-height: 1.1; }
  .contact__role { font-size: 23px; line-height: 1.1; margin-bottom: 12px; }
  .contact__line { font-size: 22px; line-height: 31px; }
  .contact__label { font-weight: 700; color: var(--navy); margin-right: 6px; }

  .back-brand {
    position: absolute; left: 182px; top: 196px;
    display: flex; align-items: center; gap: 22px;
  }
  .back-brand .brand-mark { width: 94px; height: 94px; border-radius: 12px; margin: 0; }
  .back-brand .brand-name { font-size: 92px; margin: 0; letter-spacing: 2px; }
</style>
</head>
<body>
  <section class="card card--front">
    <svg class="card__decor" viewBox="0 0 831 489" preserveAspectRatio="none" aria-hidden="true">
      <defs>
        <linearGradient id="wave" x1="0" y1="0" x2="1" y2="0">
          <stop offset="0" stop-color="#1aa0db"/>
          <stop offset="1" stop-color="#1f5a9a"/>
        </linearGradient>
      </defs>
      <polygon points="460,489 831,300 831,360 560,489" fill="var(--haze)" opacity="0.6"/>
      <polygon points="600,489 831,380 831,489" fill="var(--haze)" opacity="0.5"/>
      <path d="M300,0 C520,10 650,40 831,0 L831,30 C700,50 560,10 300,0 Z" fill="url(#wave)"/>
      <path d="M0,489 L0,470 C60,450 170,455 260,470 C330,480 390,485 440,489 Z" fill="url(#wave)"/>
    </svg>
    <div class="brand-block">
      <div class="brand-mark"></div>
      <div class="brand-name">NOVKA</div>
    </div>
    <div class="divider"></div>
    <div class="contact">
      <p class="contact__name">Marcus Ellery</p>
      <p class="contact__role">Executive</p>
      <p class="contact__line">2710 Harbor Lane</p>
      <p class="contact__line">Suite 318, Coral Bay</p>
      <p class="contact__line">FL 33021</p>
      <p class="contact__line"><span class="contact__label">Ph:</span> (555) 214-0938</p>
      <p class="contact__line"><span class="contact__label">Cell:</span>(555) 670-4182</p>
      <p class="contact__line"><span class="contact__label">Email:</span>hello@novka.com</p>
      <p class="contact__line"><span class="contact__label">Web:</span>www.novka.com</p>
    </div>
  </section>

  <section class="card card--back">
    <svg class="card__decor" viewBox="0 0 831 486" preserveAspectRatio="none" aria-hidden="true">
      <polygon points="0,0 260,0 0,150" fill="var(--haze)" opacity="0.7"/>
      <polygon points="0,0 120,0 0,70" fill="var(--haze)" opacity="0.6"/>
      <polygon points="530,486 831,300 831,350 610,486" fill="var(--haze)" opacity="0.6"/>
      <polygon points="660,486 831,390 831,486" fill="var(--haze)" opacity="0.5"/>
    </svg>
    <div class="back-brand">
      <div class="brand-mark"></div>
      <div class="brand-name">NOVKA</div>
    </div>
  </section>
</body>
</html>
```